Business Card Design

The attached file is what i need on the front of the card. No details to be changed.

On the back could i have as a heading:
We buy for cash $$$
Deceased estates house lots
Antiques, vintage furniture, bikes, kitchenware, automobile, toys,
sports memorabilia, books, records, signage,farm equipment and fashion.

Industry/Entity Type

House

```html
<!DOCTYPE html>
<html lang="en">
<head>
<meta charset="utf-8">
<title>Kestrel Row Vintage – Business Card</title>
<link rel="stylesheet" href="https://fonts.googleapis.com/css2?family=Ubuntu:wght@400;500;700&family=Lobster+Two:ital,wght@1,700&family=Rye&family=Courier+Prime&display=swap">
<style>
  :root {
    --red: #e8202a;
    --red-deep: #c8141d;
    --yellow: #fdd22e;
    --ink: #1d1a17;
    --white: #ffffff;
    --paper: #fbfbfb;
    --label: #a9a9a9;
    --rule: #444444;
  }
  * { box-sizing: border-box; margin: 0; padding: 0; }
  html, body { width: 1200px; height: 818px; overflow: hidden; background: var(--paper); }
  .sheet { position: relative; width: 1200px; height: 818px; }

  .side-label {
    position: absolute; left: 28px;
    font: 400 20px "Courier Prime", monospace; color: var(--label); letter-spacing: 1px;
  }
  .side-label--front { top: 24px; }
  .side-label--back { top: 452px; }

  .card {
    position: absolute; left: 25px; width: 509px; height: 290px;
    border: 1px solid var(--rule); overflow: hidden; background: var(--white);
    font-family: "Ubuntu", sans-serif;
  }
  .card--front { top: 51px; }
  .card--back { top: 481px; background: var(--red); }

  /* front */
  .front__band {
    position: absolute; left: 0; top: 0; width: 100%; height: 179px; background: var(--red);
  }
  .front__name {
    position: absolute; left: 0; right: 0; top: 48px; text-align: center;
    font: 700 40px "Ubuntu", sans-serif; color: var(--yellow); letter-spacing: 0.5px;
  }
  .front__tagline {
    position: absolute; left: 0; right: 0; top: 144px; text-align: center;
    font: italic 700 21px "Lobster Two", cursive; color: var(--white); letter-spacing: 0.5px;
  }
  .hours { position: absolute; left: 25px; top: 186px; }
  .hours__open { font: 500 17px "Ubuntu", sans-serif; color: var(--red); letter-spacing: 0.3px; }
  .hours__line { font: 400 14px "Ubuntu", sans-serif; color: var(--ink); padding-left: 27px; line-height: 17px; }
  .address { position: absolute; left: 25px; top: 246px; font-size: 11px; line-height: 15px; color: var(--ink); }
  .web {
    position: absolute; right: 24px; top: 188px; display: flex; align-items: center; gap: 6px;
    font: 700 12px "Ubuntu", sans-serif; color: var(--ink);
  }
  .web__square { width: 20px; height: 20px; background: var(--red); }
  .phones {
    position: absolute; right: 24px; top: 246px; text-align: right;
    font: 700 12.5px "Ubuntu", sans-serif; color: var(--ink); line-height: 16px; letter-spacing: 0.3px;
  }

  /* back */
  .back__header { position: absolute; left: 0; top: 0; width: 100%; height: 105px; }
  .back__heading {
    position: absolute; left: 0; right: 0; top: 26px; text-align: center;
    font: 400 35px "Rye", serif; color: var(--ink); letter-spacing: 0.5px;
  }
  .buy-list {
    position: absolute; top: 108px; list-style: none;
    font: 400 17.5px "Ubuntu", sans-serif; color: var(--white); line-height: 21.7px; letter-spacing: 0.4px;
  }
  .buy-list--left { left: 25px; width: 240px; }
  .buy-list--right { left: 280px; width: 220px; }
  .buy-list li { position: relative; padding-left: 14px; }
  .buy-list li::before {
    content: ""; position: absolute; left: 2px; top: 11px;
    width: 6px; height: 6px; border-radius: 50%; background: var(--white);
  }
</style>
</head>
<body>
<main class="sheet">
  <p class="side-label side-label--front">Front</p>

  <section class="card card--front" aria-label="Business card front">
    <div class="front__band"></div>
    <h1 class="front__name">Kestrel Row Vintage</h1>
    <p class="front__tagline">Vintage - Retro Clothing &amp; Collectables</p>

    <div class="hours">
      <p class="hours__open">OPEN 6 DAYS A WEEK</p>
      <p class="hours__line">10:00am - 5:00pm</p>
      <p class="hours__line">CLOSED TUESDAYS</p>
    </div>
    <p class="address">27 Orchard Ridge Rd. Merrowvale 3920<br>Email: info@kestrelrowvintage.com.au</p>

    <p class="web">www.kestrelrowvintage.com.au <span class="web__square"></span></p>
    <p class="phones">Phone: 59 000 418<br>Mobile: 0400 552 917</p>
  </section>

  <p class="side-label side-label--back">Back</p>

  <section class="card card--back" aria-label="Business card back">
    <svg class="back__header" viewBox="0 0 509 105" preserveAspectRatio="none" aria-hidden="true">
      <path d="M0 0 H509 V70 Q254 105 0 86 Z" fill="var(--yellow)"/>
      <path d="M0 86 Q254 105 509 70" fill="none" stroke="var(--ink)" stroke-width="3"/>
    </svg>
    <h2 class="back__heading">WE BUY FOR CASH $$$</h2>

    <ul class="buy-list buy-list--left">
      <li>Deceased estates house lots</li>
      <li>Antiques</li>
      <li>Vintage furniture</li>
      <li>Bikes</li>
      <li>Kitchenware</li>
      <li>Automobile</li>
    </ul>
    <ul class="buy-list buy-list--right">
      <li>Toys</li>
      <li>Sports memorabilia</li>
      <li>Books</li>
      <li>Records</li>
      <li>Signage</li>
      <li>Farm equipment and fashion</li>
    </ul>
  </section>
</main>
</body>
</html>
```